Meadowlark Learning Growth Partners (MLGP)

This is a professional business card. Logo and picture are a must on the front of the card. I am an educational consultant. I have been consulting for the past three years for a company. I am now opening my own company. My goal for my consulting company is to eventually consult all over America.

Target Market(s)

Educators, schools, professionals

Industry/Entity Type

Consulting

Contact Information for Business Card

Picture/logo on front, simple modern design

Font styles to use
Serif

Colors
85abd2
0355a3
3176b5
cedeed

Requirements
Must have
• picture, logo,
• Odessa Pruitt, Ed.S
• address 5073 Cormorant ridge Dr. Nashville, TN 37940
• Cell:616-555-0148
• Office: 629-555-0172
• www.Mlgpedu.example
• pruittodessa@mailbox.example

```html
<!DOCTYPE html>
<html lang="en">
<head>
<meta charset="utf-8">
<title>MLGP Business Card</title>
<link href="https://fonts.googleapis.com/css2?family=Montserrat:wght@700&family=Arimo:wght@400;700&display=swap" rel="stylesheet">
<style>
  :root{
    --navy:#1f3a7a;
    --blue-dark:#2c4a8a;
    --blue:#4264ac;
    --paper:#f7f7f7;
    --ink:#222;
    --ring:#e3e3e3;
    --bg:#cfced2;
  }
  *{margin:0;padding:0;box-sizing:border-box}
  html,body{width:1200px;height:990px;overflow:hidden}
  body{background:var(--bg);position:relative;font-family:"Arimo",Arial,sans-serif}
  .card{position:absolute;left:220px;width:760px;height:423px;border-radius:22px;overflow:hidden;box-shadow:0 6px 14px rgba(0,0,0,.22)}
  .card--front{top:50px;background:var(--paper)}
  .card--back{top:517px;background:linear-gradient(100deg,var(--blue-dark),var(--blue))}
  .front__band{position:absolute;left:575px;top:0;right:0;bottom:0;background:linear-gradient(90deg,var(--blue-dark),var(--blue))}
  .front__ring{position:absolute;left:436px;top:78px;width:274px;height:274px;border-radius:50%;background:var(--paper);border:4px solid var(--ring)}
  .front__photo{position:absolute;left:450px;top:92px;width:246px;height:246px;border-radius:50%;background:radial-gradient(circle at 50% 40%,#d9c9a8 0 30%,#5a7fd0 55%,#3d63b8 100%)}
  .brand{position:absolute;left:44px;top:44px;display:flex;align-items:center}
  .brand__mark{width:34px;height:34px;border-radius:50%;background:var(--navy);margin-right:12px}
  .brand__name{font-family:"Montserrat",sans-serif;font-weight:700;font-size:36px;letter-spacing:4px;color:var(--navy)}
  .brand__rule{width:2px;height:88px;background:var(--navy);margin:0 14px 0 16px}
  .brand__tagline{font-family:"Montserrat",sans-serif;font-weight:700;font-size:18px;line-height:24px;color:var(--navy)}
  .person{position:absolute;left:44px;top:188px;font-size:24px;color:var(--navy);font-weight:700}
  .person__title{font-weight:400}
  .contact{position:absolute;left:44px;top:236px;list-style:none;font-size:17px;color:var(--ink)}
  .contact li{display:flex;align-items:center;height:25px}
  .contact svg{width:16px;height:16px;margin-right:12px;fill:none;stroke:var(--navy);stroke-width:2}
  .address{position:absolute;left:44px;top:352px;font-size:17px;line-height:23px;color:var(--ink)}
  .back__name{position:absolute;left:0;right:0;top:170px;text-align:center;font-family:"Montserrat",sans-serif;font-weight:700;font-size:64px;letter-spacing:8px;color:#fff}
</style>
</head>
<body>
  <section class="card card--front">
    <div class="front__band"></div>
    <div class="front__ring"></div>
    <div class="front__photo" role="img" aria-label="Portrait photo of Odessa Pruitt"></div>

    <div class="brand">
      <span class="brand__mark"></span>
      <span class="brand__name">MLGP</span>
      <span class="brand__rule"></span>
      <span class="brand__tagline">Meadowlark<br>Learning<br>Growth<br>Partners</span>
    </div>

    <p class="person">ODESSA PRUITT, <span class="person__title">Ed.S</span></p>

    <ul class="contact">
      <li><svg viewBox="0 0 16 16"><rect x="4" y="1" width="8" height="14" rx="2"/></svg>616-555-0148</li>
      <li><svg viewBox="0 0 16 16"><path d="M4 1.5 2.5 3c-1 3 4.5 11 10 10.5L14 12l-3-2.5-1.5 1.2C7.5 9.5 6 8 5.3 6l1.2-1.5z" fill="#1f3a7a" stroke="none"/></svg>629-555-0172</li>
      <li><svg viewBox="0 0 16 16"><rect x="1" y="3" width="14" height="10"/><path d="m1 3 7 6 7-6"/></svg>pruittodessa@mailbox.example</li>
      <li><svg viewBox="0 0 16 16"><circle cx="8" cy="8" r="6.5"/><path d="M1.5 8h13M8 1.5c-3 3.5-3 9.5 0 13M8 1.5c3 3.5 3 9.5 0 13"/></svg>www.Mlgpedu.example</li>
    </ul>

    <p class="address">5073 Cormorant ridge<br>Dr. Nashville, TN 37940</p>
  </section>

  <section class="card card--back">
    <p class="back__name">MLGP</p>
  </section>
</body>
</html>
```